Premium label design for product needed

UPDATE: (Scroll down)
For a face care product i need a new front label on the bottle. The current one is white and i want to add the franchise color green. The objective is to premiunize the packaging and to give guidance to the consumers to find their franchise color. The task is to find several option to color the label on the bottle in the most premium way. But at the same time it should not be playful, more in a serious medical direction or in a counterbrand direction. It should look absolutely premium. but should not shout to much. The text structure should remain the same. I will provide a powerpoint slide to illustrate the task even clearer.
UPDATE: DO NOT DESIGN THE FOLDING BOX, only design the bottle. The folding box only serves the purpose of giving the text/layout structure and rough color intent.

Target Market(s)

female 25-39

Requirements
Must have
• Premium, Uniqueness, Innovative

```html
<!DOCTYPE html>
<html lang="en">
<head>
<meta charset="UTF-8">
<title>Neo Derm Cleanser — Front Label</title>
<link rel="stylesheet" href="https://fonts.googleapis.com/css2?family=Montserrat:wght@400;500;800&display=swap">
<style>
  :root {
    --label-green: #b5e3bf;
    --band-dark: #5c9f73;
    --band-mid: #8cc59c;
    --band-light: #e2f3e7;
    --ink: #0c0c0c;
    --flourish: #f4fbf6;
  }
  html, body {
    margin: 0;
    padding: 0;
    width: 1200px;
    height: 958px;
    overflow: hidden;
    background: var(--label-green);
  }
  .label {
    position: relative;
    width: 1200px;
    height: 958px;
    background: var(--label-green);
    font-family: "Montserrat", Arial, sans-serif;
    color: var(--ink);
    overflow: hidden;
  }
  .band {
    position: absolute;
    left: 0;
    width: 100%;
    background: linear-gradient(90deg,
      var(--band-dark) 0%,
      var(--band-mid) 25%,
      var(--band-light) 50%,
      var(--band-mid) 75%,
      var(--band-dark) 100%);
  }
  .band--top {
    top: 0;
    height: 40px;
    box-shadow: inset 0 -4px 0 rgba(255,255,255,0.35);
  }
  .band--bottom {
    bottom: 0;
    height: 50px;
    box-shadow: inset 0 4px 0 rgba(255,255,255,0.35);
  }
  .product-name {
    position: absolute;
    left: 0;
    width: 100%;
    margin: 0;
    text-align: center;
    line-height: 1;
    white-space: nowrap;
    box-sizing: border-box;
  }
  .product-name__main {
    top: 183px;
    font-size: 178px;
    font-weight: 800;
    letter-spacing: 2px;
  }
  .product-name__sub {
    top: 328px;
    font-size: 152px;
    font-weight: 400;
    letter-spacing: 0.17em;
    padding-left: 0.17em;
  }
  .flourish {
    position: absolute;
    left: 408px;
    top: 512px;
    width: 387px;
    height: 44px;
    border-radius: 22px;
    background: radial-gradient(ellipse at center, var(--flourish) 0%, rgba(244,251,246,0.35) 60%, rgba(244,251,246,0) 100%);
  }
  .variant {
    position: absolute;
    left: 0;
    top: 798px;
    width: 100%;
    margin: 0;
    text-align: center;
    font-size: 74px;
    font-weight: 500;
    line-height: 1;
    letter-spacing: 1px;
    white-space: nowrap;
  }
</style>
</head>
<body>
  <main class="label">
    <div class="band band--top"></div>
    <h1 class="product-name product-name__main">NEO DERM</h1>
    <p class="product-name product-name__sub">CLEANSER</p>
    <div class="flourish" role="img" aria-label="Decorative white scroll flourish divider"></div>
    <p class="variant">D. V. CALM FLUID</p>
    <div class="band band--bottom"></div>
  </main>
</body>
</html>
```